TIDAL VERGE needs bisness cards pronto

Bisness name is "TIDAL VERGE" new bisness the bisness includes lawn mowing, garden matanace, and any jobs around the house.
I need a card that is colorful and vibrant and the bisness of lawn mowing maybe with some nature with it. It also needs my contact details"Darren Quellby mobile 0413562049 call for free quote and email norma.vance@fernmail.com.au and a catchy tag line

Industry/Entity Type

House

Requirements
Must have
• Bisness name "TIDAL VERGE"
Contact details "0413562049"
Email norma.vance@fernmail.com.au
Call for free quote

```html
<!DOCTYPE html>
<html lang="en">
<head>
<meta charset="utf-8">
<title>TIDAL VERGE – Business Cards</title>
<link rel="stylesheet" href="https://fonts.googleapis.com/css2?family=Quicksand:wght@400;500&family=Ubuntu:wght@500;700&display=swap">
<style>
  :root {
    --page: #ffffff;
    --green-deep: #1b4a06;
    --green-light: #4f7a3e;
    --maroon-deep: #5e1f1c;
    --maroon-light: #8a5552;
    --strip: rgba(255, 255, 255, 0.12);
    --white: #ffffff;
    --ink: #1c1c1c;
    --banner-dark: #222222;
  }
  * { margin: 0; padding: 0; box-sizing: border-box; }
  html, body {
    width: 1200px;
    height: 1000px;
    overflow: hidden;
    background: var(--page);
  }
  .canvas {
    position: relative;
    width: 1200px;
    height: 1000px;
  }
  .card {
    position: absolute;
    width: 620px;
    height: 354px;
    box-shadow: 0 10px 30px rgba(0, 0, 0, 0.25);
    overflow: hidden;
  }

  /* Front */
  .card-front {
    left: 50px;
    top: 90px;
    background: linear-gradient(150deg, var(--green-deep) 35%, var(--green-light) 100%);
    color: var(--white);
    text-align: center;
  }
  .front-name {
    position: absolute;
    left: 0; right: 0;
    top: 112px;
    font-family: "Quicksand", sans-serif;
    font-weight: 500;
    font-size: 58px;
    letter-spacing: 3px;
  }
  .front-services {
    position: absolute;
    left: 0; right: 0;
    top: 190px;
    font-family: "Quicksand", sans-serif;
    font-weight: 500;
    font-size: 16px;
    letter-spacing: 0.5px;
  }

  /* Back */
  .card-back {
    left: 530px;
    top: 570px;
    background: linear-gradient(150deg, var(--maroon-deep) 40%, var(--maroon-light) 100%);
    color: var(--white);
    font-family: "Ubuntu", sans-serif;
  }
  .name-banner {
    position: absolute;
    left: 0;
    top: 34px;
    width: 370px;
    height: 42px;
    background: var(--white);
    clip-path: polygon(0 0, 340px 0, 100% 100%, 0 100%);
    padding-left: 26px;
    line-height: 42px;
    color: var(--maroon-deep);
    font-weight: 700;
    font-size: 28px;
  }
  .quote-label {
    position: absolute;
    left: 22px;
    top: 108px;
    font-size: 13px;
    font-weight: 500;
    color: var(--ink);
  }
  .phone {
    position: absolute;
    left: 20px;
    top: 120px;
    font-size: 34px;
    font-weight: 700;
    letter-spacing: 1px;
  }
  .email {
    position: absolute;
    left: 20px;
    top: 170px;
    font-size: 23px;
    font-weight: 500;
    letter-spacing: 0.5px;
  }
  .brand-banner {
    position: absolute;
    right: 0;
    top: 245px;
    width: 270px;
    height: 40px;
    background: var(--banner-dark);
    clip-path: polygon(30px 0, 100% 0, 100% 100%, 0 100%);
    padding-right: 20px;
    text-align: right;
    line-height: 40px;
    font-family: "Quicksand", sans-serif;
    font-weight: 500;
    font-size: 27px;
    letter-spacing: 1px;
  }
  .services-strip {
    position: absolute;
    left: 0; right: 0;
    top: 285px;
    height: 38px;
    background: var(--strip);
    text-align: center;
    line-height: 38px;
    font-family: "Quicksand", sans-serif;
    font-weight: 500;
    font-size: 16px;
    letter-spacing: 0.5px;
  }
</style>
</head>
<body>
<main class="canvas">
  <section class="card card-front" aria-label="Business card front">
    <h1 class="front-name">TIDAL VERGE</h1>
    <p class="front-services">lawn mowing | garden matanace | any jobs around the house</p>
  </section>

  <section class="card card-back" aria-label="Business card back">
    <div class="name-banner">Darren Quellby</div>
    <p class="quote-label">call for free quote</p>
    <p class="phone">0413562049</p>
    <p class="email">norma.vance@fernmail.com.au</p>
    <div class="brand-banner">TIDAL VERGE</div>
    <p class="services-strip">lawn mowing | garden matanace | any jobs around the house</p>
  </section>
</main>
</body>
</html>
```